Bref créative
Bright Harbor Living :: Marketing Materials (postcard, one sided flyer, door hangers)
Senior Referrals for Quality Living
"Assistance when you need it most"
I am looking for postcard and single sided flyer and door hanger. I need the brochure to gain Attention, cause Interest, cause the Desire to use my referral service and call them into Action by picking up their phone and calling me for information in regards to placement into an assisted living facility or care home.
This must be simple so that the elderly can read the information and process it.
Health
Young adults to older adults and their elderly parents who need support and assisted care.
Please color coordinate your designs with the main logo.
bright harbor living

```html
<!DOCTYPE html>
<html lang="en">
<head>
<meta charset="utf-8">
<title>Bright Harbor Living – Marketing Set</title>
<link href="https://fonts.googleapis.com/css2?family=Lato:wght@400;700;900&family=Lora:ital,wght@1,700&display=swap" rel="stylesheet">
<style>
:root{
  --navy:#1c3c78;
  --blue:#2d5aa6;
  --blue-light:#4f7fc8;
  --red:#c8202a;
  --ink:#2b2b2b;
  --paper:#ffffff;
  --stage:#ece7de;
  --label:#3a3a3a;
  --photo-a:#c9b9a6;
  --photo-b:#8fa7c4;
}
*{box-sizing:border-box;margin:0;padding:0}
html,body{width:1200px;height:751px;overflow:hidden}
body{background:var(--stage);font-family:'Lato',sans-serif;color:var(--ink);position:relative}
.piece-label{position:absolute;font-size:11px;font-weight:700;color:var(--label);text-align:center;line-height:1.2}
.piece-label small{display:block;font-size:9px;font-weight:400}
.piece{position:absolute;background:var(--paper);box-shadow:0 2px 6px rgba(0,0,0,.25);overflow:hidden}
.tagline{font-family:'Lora',serif;font-style:italic;font-weight:700;color:var(--red);text-align:center;white-space:nowrap}
.brand{display:flex;align-items:center;gap:6px;font-weight:900;color:var(--navy);line-height:1;white-space:nowrap}
.brand-dot{border-radius:50%;background:var(--blue);flex:none}
.brand-sub{color:var(--navy);font-weight:700;white-space:nowrap}
.photo{background:linear-gradient(135deg,var(--photo-a),var(--photo-b))}
.band{background:linear-gradient(180deg,var(--blue-light),var(--navy));color:#fff}
.ticks{list-style:none}
.ticks li{position:relative;padding-left:12px}
.ticks li::before{content:"";position:absolute;left:0;top:.3em;width:6px;height:6px;background:var(--red);border-radius:50%}

/* door hanger */
.hanger{left:14px;top:72px;width:118px;height:420px;border-radius:6px}
.hanger-hole{position:absolute;left:31px;top:14px;width:56px;height:56px;border-radius:50%;border:1px solid #b9b9b9;background:var(--stage)}
.hanger .tagline{position:absolute;top:80px;left:0;right:0;font-size:6px}
.hanger .brand{position:absolute;top:94px;left:8px;font-size:10px}
.hanger .brand-sub{position:absolute;top:108px;left:8px;font-size:5.5px}
.hanger .photo{position:absolute;top:122px;left:0;width:118px;height:112px}
.hanger .band{position:absolute;top:234px;left:0;width:118px;height:186px;padding:8px 7px}
.hanger-head{font-size:6.5px;font-weight:700;line-height:1.3;text-align:center;margin-bottom:6px}
.hanger .ticks{font-size:5.5px;line-height:1.6}
.hanger-contact{position:absolute;left:10px;right:10px;bottom:8px;background:#fff;color:var(--navy);border-radius:3px;padding:4px;text-align:center;font-size:5.5px;line-height:1.35}
.hanger-contact strong{font-size:8px;display:block}

/* postcard front */
.pc-front{left:211px;top:67px;width:365px;height:245px}
.pc-front .tagline{position:absolute;top:10px;left:0;right:0;font-size:11px}
.pc-front-copy{position:absolute;top:32px;left:22px;width:320px;font-size:5.8px;line-height:1.45}
.pc-front-copy p{margin-bottom:5px}
.pc-front .brand{position:absolute;top:168px;left:18px;font-size:15px}
.pc-front .brand-sub{position:absolute;top:188px;left:40px;font-size:7px}
.pc-front .photo{position:absolute;top:118px;right:0;width:165px;height:107px}
.pc-front-strip{position:absolute;bottom:0;left:0;right:0;height:20px}

/* postcard back */
.pc-back{left:211px;top:360px;width:365px;height:264px}
.pc-back .band{position:absolute;inset:0}
.pc-back-head{position:absolute;top:12px;left:14px;right:14px;text-align:center;font-size:9.5px;font-weight:700;line-height:1.35}
.pc-back .photo{position:absolute;top:56px;left:14px;width:150px;height:150px}
.pc-back .ticks{position:absolute;top:70px;left:178px;width:180px;font-size:8px;line-height:1.9}
.pc-back-web{position:absolute;bottom:12px;left:0;right:0;text-align:center;font-size:11px;font-weight:900}

/* flyer */
.flyer{left:595px;top:43px;width:588px;height:677px}
.flyer-photo-top{position:absolute;top:0;left:0;width:175px;height:140px}
.flyer .tagline{position:absolute;top:12px;left:185px;right:10px;font-size:19px}
.flyer .brand{position:absolute;top:52px;left:232px;font-size:30px}
.flyer .brand-sub{position:absolute;top:90px;left:270px;font-size:13px}
.flyer-offer{position:absolute;top:140px;left:0;width:588px;height:162px}
.flyer-offer h2{position:absolute;top:12px;left:14px;width:340px;font-size:11.5px;line-height:1.3}
.flyer-offer .ticks{position:absolute;top:50px;left:22px;width:330px;font-size:10px;line-height:1.55}
.flyer-offer .photo{position:absolute;top:0;right:0;width:220px;height:162px}
.flyer-process{position:absolute;top:310px;left:14px;right:14px;height:26px;background:var(--navy);color:#fff;text-align:center;font-size:15px;font-weight:900;line-height:26px;border-radius:2px}
.flyer-copy{position:absolute;top:344px;left:20px;right:20px;font-size:7.2px;line-height:1.45}
.flyer-copy h3{font-size:7.5px;font-weight:900;color:var(--navy);text-transform:uppercase;margin-top:7px}
.flyer-copy ul{list-style:none;margin-top:2px}
.flyer-footer{position:absolute;bottom:0;left:0;right:0;height:44px}
.flyer-footer p{position:absolute;left:16px;top:16px;font-size:7px}
.flyer-contact{position:absolute;right:12px;top:-18px;width:120px;height:56px;background:#fff;border:1px solid var(--blue);border-radius:3px;color:var(--navy);text-align:center;padding-top:6px;font-size:7px;line-height:1.3}
.flyer-contact strong{display:block;font-size:14px;font-weight:900;margin-top:3px}
</style>
</head>
<body>

<div class="piece-label" style="left:8px;top:30px;width:130px">Door Hangers<small>(3.5 inch x 8.5 inch)</small></div>
<div class="piece-label" style="left:300px;top:40px;width:190px">Postcard (Front)<small>(4 inch x 6 inch)</small></div>
<div class="piece-label" style="left:300px;top:330px;width:190px">Postcard (Back)<small>(4 inch x 6 inch)</small></div>
<div class="piece-label" style="left:1000px;top:10px;width:190px">One Sided Flyer<small>(8 inch x 11 inch)</small></div>

<!-- Door hanger -->
<section class="piece hanger">
  <div class="hanger-hole"></div>
  <p class="tagline">"Assistance when you need it most"</p>
  <div class="brand"><span class="brand-dot" style="width:7px;height:7px"></span>Bright Harbor Living</div>
  <p class="brand-sub">Senior Referrals for Quality Living</p>
  <div class="photo" role="img" aria-label="Photo of a smiling senior couple"></div>
  <div class="band">
    <p class="hanger-head">We provide a free service to assist seniors find quality care that will go above and beyond expectations</p>
    <ul class="ticks">
      <li>Medical &amp; non-medical in-home care</li>
      <li>Retirement / Independent living</li>
      <li>Assisted living facilities</li>
      <li>Specialized memory care</li>
      <li>Skilled nursing facilities</li>
      <li>Multi-level care facilities</li>
    </ul>
    <div class="hanger-contact">Please Contact:<br>Dana Whitfield<br>To help find your loved one a home<strong>555-014-2276</strong></div>
  </div>
</section>

<!-- Postcard front -->
<section class="piece pc-front">
  <p class="tagline">"Assistance when you need it most"</p>
  <div class="pc-front-copy">
    <p>We help families find trusted assisted living and care homes for the people they love. Our caring team listens, visits homes and guides you at each step.</p>
    <p>Our service is free to families. We match needs, budget and location so your loved one feels safe and at home.</p>
    <p>Call today to talk with a local advisor about placement options.</p>
  </div>
  <div class="brand"><span class="brand-dot" style="width:12px;height:12px"></span>Bright Harbor Living</div>
  <p class="brand-sub">Senior Referrals for Quality Living</p>
  <div class="photo" role="img" aria-label="Photo of a senior woman with her daughter"></div>
  <div class="pc-front-strip band"></div>
</section>

<!-- Postcard back -->
<section class="piece pc-back">
  <div class="band">
    <p class="pc-back-head">We provide a free service to assist seniors find quality care that will go above and beyond expectations</p>
    <div class="photo" role="img" aria-label="Photo of a senior couple smiling together"></div>
    <ul class="ticks">
      <li>Medical &amp; non-medical in-home care services</li>
      <li>Retirement / Independent living facilities</li>
      <li>Assisted living facilities</li>
      <li>Specialized memory care facilities</li>
      <li>Skilled nursing facilities</li>
      <li>Multi-level care/Continuing care facilities</li>
    </ul>
    <p class="pc-back-web">www.BrightHarborLiving.com</p>
  </div>
</section>

<!-- Flyer -->
<section class="piece flyer">
  <div class="flyer-photo-top photo" role="img" aria-label="Photo of a happy senior couple"></div>
  <p class="tagline">"Assistance when you need it most"</p>
  <div class="brand"><span class="brand-dot" style="width:22px;height:22px"></span>Bright Harbor Living</div>
  <p class="brand-sub">Senior Referrals for Quality Living</p>

  <div class="flyer-offer band">
    <h2>We provide a free service to assist seniors find quality care that will go above and beyond expectations</h2>
    <ul class="ticks">
      <li>Medical &amp; non-medical in-home care services</li>
      <li>Retirement / Independent living facilities</li>
      <li>Assisted living facilities</li>
      <li>Specialized memory care facilities</li>
      <li>Skilled nursing facilities</li>
      <li>Multi-level care/Continuing care facilities</li>
    </ul>
    <div class="photo" role="img" aria-label="Photo of a caregiver with a senior woman"></div>
  </div>

  <div class="flyer-process">Bright Harbor Living's Process</div>
  <div class="flyer-copy">
    <p>Our goal is to help families find the right home for each senior. We listen closely, learn about needs and wishes, and visit every option with you so the move feels calm and clear.</p>
    <h3>Selection</h3>
    <p>We visit and review homes in your area, checking care, safety, staff and comfort so we only suggest places we trust.</p>
    <h3>Assessment</h3>
    <p>We meet with your family to learn about health, daily needs, budget and the place your loved one hopes to live.</p>
    <h3>Support</h3>
    <p>We stay with you through tours, paperwork and move in day, and we check in after to make sure all is well.</p>
    <h3>Payment</h3>
    <p>Our service is free to you. Homes pay us a referral fee, so families never receive a bill from us.</p>
    <ul>
      <li>Ask us about:</li>
      <li>Private pay</li>
      <li>Long term care insurance</li>
      <li>Veterans benefits</li>
      <li>Medi-Cal programs</li>
    </ul>
  </div>

  <div class="flyer-footer band">
    <p>4410 Harbor Rd, Ste 2 • Oakdale, CA 94000 • info@brightharborliving.com</p>
    <div class="flyer-contact">Please Contact:<br>Dana Whitfield<strong>555-014-2276</strong></div>
  </div>
</section>

</body>
</html>
```